Business Card Design

I am a Special Event Consultant,I arrange and organise Special Events - Product Launches,Sponsorship and Product Displays.

I would like the RTV to be a feature of the design with 'Special Event Services" underneath - keep it very simple but creative using this information. So it is just the letters "RTV" with Event Services underneath.

(Simple Colours - Silver, Black, Grey - no bright colours - We work for Valtoria Drenn,KDX, Lyndrel So it is class and classic.)

Only my Name and mobile on the front.

Contact Information for Business Card

FRONT
Tess Varnholt
Tel: 0436 218907

BACK
Email: tess@rtveventservices.example.au

2807 Wexbury Heights,83 Pollard Street
NORTHVALE.Vic.3158.

```html
<!DOCTYPE html>
<html lang="en">
<head>
<meta charset="utf-8">
<title>RTV Event Services – Business Card</title>
<link rel="stylesheet" href="https://fonts.googleapis.com/css2?family=Oswald:wght@500;600&family=Open+Sans:wght@400&display=swap">
<style>
  :root {
    --page: #e9e7e3;
    --card-top: #3a3a3c;
    --card-mid: #1c1c1d;
    --card-bottom: #0b0b0c;
    --silver: #d9d9db;
    --silver-soft: #b9b9bc;
    --rule: #55565a;
  }
  * { margin: 0; padding: 0; box-sizing: border-box; }
  html, body {
    width: 1200px;
    height: 1023px;
    overflow: hidden;
    background: var(--page);
  }
  .sheet {
    width: 1200px;
    height: 1023px;
    display: flex;
    flex-direction: column;
    align-items: center;
    justify-content: center;
    gap: 40px;
  }
  .card {
    position: relative;
    width: 760px;
    height: 463px;
    border-radius: 26px;
    background: linear-gradient(160deg, var(--card-top) 0%, var(--card-mid) 45%, var(--card-bottom) 100%);
    box-shadow: 0 10px 28px rgba(0, 0, 0, 0.28);
    overflow: hidden;
    color: var(--silver);
  }

  /* Card with brand, email and address */
  .brand {
    position: absolute;
    left: 110px;
    top: 190px;
    font-family: "Oswald", sans-serif;
    font-weight: 500;
    font-size: 44px;
    line-height: 1.1;
    letter-spacing: 1px;
    text-transform: uppercase;
    color: var(--silver);
  }
  .email {
    position: absolute;
    left: 40px;
    bottom: 34px;
    font-family: "Open Sans", sans-serif;
    font-size: 17px;
    color: var(--silver-soft);
  }
  .address {
    position: absolute;
    right: 40px;
    top: 34px;
    text-align: right;
    font-family: "Open Sans", sans-serif;
    font-size: 17px;
    line-height: 1.55;
    color: var(--silver-soft);
  }

  /* Card with name and mobile */
  .rule {
    position: absolute;
    left: 0;
    right: 0;
    top: 214px;
    height: 2px;
    background: var(--rule);
  }
  .person {
    position: absolute;
    left: 190px;
    top: 170px;
    padding: 0 24px;
    background: var(--card-mid);
  }
  .person-name {
    font-family: "Oswald", sans-serif;
    font-weight: 600;
    font-size: 58px;
    line-height: 1.1;
    letter-spacing: 1px;
    text-transform: uppercase;
    color: var(--silver);
  }
  .person-phone {
    margin-top: 10px;
    font-family: "Oswald", sans-serif;
    font-weight: 500;
    font-size: 38px;
    line-height: 1;
    letter-spacing: 2px;
    color: var(--silver-soft);
  }
</style>
</head>
<body>
  <main class="sheet">
    <section class="card card-back" aria-label="Card back">
      <div class="brand">
        <div class="brand-name">RTV</div>
        <div class="brand-tagline">Event Services</div>
      </div>
      <p class="address">2807 Wexbury Heights<br>83 Pollard Street, NORTHVALE.Vic.3158</p>
      <p class="email">tess@rtveventservices.example.au</p>
    </section>

    <section class="card card-front" aria-label="Card front">
      <span class="rule"></span>
      <div class="person">
        <div class="person-name">Tess Varnholt</div>
        <div class="person-phone">0436 218907</div>
      </div>
    </section>
  </main>
</body>
</html>
```